Tobin's Jewelry Studio Needs a Moving Location Flyer

We need a flyer to inform our customers of our location moving. We will be moving to our city's downtown which is only 1 mile away from our current address. We will be having a moving sale ( Up to 80% off). The sale starts Sept. 8th Our business creates, sells, and repairs fine jewelry. Dimensions are 5"x8"

Target Market(s)

Women ages 25-55

Industry/Entity Type

Jewelry

Colors
85abd2
cfdeed

Requirements
Must have
• Our logo
• Mention of the sale
• Our current address
• 4785 Cresthaven Blvd.
• Dunmore, Ca 94318
• (415)826-3319
Nice to have
• Mention that we're relocating to downtown Dunmore (new location opening Nov. 1st.)

```html
<!DOCTYPE html>
<html lang="en">
<head>
<meta charset="utf-8">
<title>Tobin's Jewelry Studio – Moving Sale</title>
<link rel="stylesheet" href="https://fonts.googleapis.com/css2?family=Playfair+Display:wght@400;700;900&display=swap">
<style>
  :root {
    --sky: #bfe2e8;
    --paper: #ffffff;
    --ink: #3c3c3c;
    --frame: #3a1f1a;
    --shadow: rgba(0, 0, 0, 0.18);
  }
  * { margin: 0; padding: 0; box-sizing: border-box; }
  html, body { width: 800px; height: 1200px; overflow: hidden; background: var(--paper); }
  .flyer {
    position: relative; width: 800px; height: 1200px; overflow: hidden;
    background: var(--paper); color: var(--ink);
    font-family: "Playfair Display", Georgia, serif;
  }
  .sky-band { position: absolute; left: 0; top: 0; width: 800px; height: 696px; background: var(--sky); }
  .logo-cap {
    position: absolute; left: 180px; top: -250px; width: 440px; height: 440px;
    border-radius: 50%; background: var(--paper);
  }
  .frame { position: absolute; inset: 0; pointer-events: none; }
  .brand {
    position: absolute; left: 0; right: 0; top: 46px;
    display: flex; justify-content: center; align-items: center; gap: 10px;
    font-size: 20px; font-weight: 700; color: var(--ink);
  }
  .brand-dot { width: 16px; height: 16px; border-radius: 50%; background: var(--sky); }
  .sale-disc {
    position: absolute; left: 120px; top: 180px; width: 560px; height: 560px;
    border-radius: 50%; background: var(--sky);
    border: 10px solid var(--paper);
    box-shadow: 0 10px 14px var(--shadow);
  }
  .start-disc {
    position: absolute; left: 548px; top: 525px; width: 162px; height: 162px;
    border-radius: 50%; background: var(--sky);
    border: 6px solid var(--paper);
    display: flex; flex-direction: column; align-items: center; justify-content: center;
  }
  .start-label { font-size: 19px; font-weight: 700; line-height: 1; }
  .start-date { font-size: 29px; line-height: 1.1; }
  .center { position: absolute; left: 0; right: 0; text-align: center; }
  .sale-kicker { top: 304px; font-size: 54px; letter-spacing: 9px; line-height: 1; padding-left: 9px; }
  .sale-word { top: 334px; font-size: 172px; line-height: 1; letter-spacing: 2px; }
  .sale-upto { top: 518px; font-size: 34px; letter-spacing: 7px; line-height: 1; padding-left: 7px; }
  .sale-amount {
    position: absolute; left: 283px; top: 556px;
    display: flex; align-items: flex-end; line-height: 1;
  }
  .sale-number { font-size: 108px; font-weight: 700; letter-spacing: -2px; }
  .sale-off { display: flex; flex-direction: column; margin-left: 6px; margin-bottom: 14px; }
  .sale-percent { font-size: 28px; line-height: 1; }
  .sale-offword { font-size: 31px; letter-spacing: 5px; line-height: 1; }
  .heading { font-weight: 700; line-height: 1; }
  .move-heading { top: 760px; font-size: 33px; letter-spacing: 7px; padding-left: 7px; }
  .move-text { top: 820px; font-size: 26px; line-height: 34px; }
  .location-heading { top: 932px; font-size: 25px; letter-spacing: 6px; padding-left: 6px; }
  .address { top: 988px; font-size: 19px; line-height: 1; }
  .phone { top: 1017px; font-size: 27px; line-height: 1; }
  .opening { top: 1060px; font-size: 18px; line-height: 1; }
  .tagline { top: 1130px; font-size: 16px; letter-spacing: 6px; padding-left: 6px; line-height: 1; }
</style>
</head>
<body>
<main class="flyer">
  <div class="sky-band"></div>
  <div class="logo-cap"></div>

  <svg class="frame" width="800" height="1200" viewBox="0 0 800 1200">
    <g stroke="var(--frame)" stroke-width="2" fill="none">
      <polyline points="240,61 36,61 36,1160 765,1160 765,61 560,61"/>
    </g>
    <g class="divider" stroke="var(--ink)" stroke-width="2" fill="var(--ink)">
      <line x1="105" y1="807" x2="695" y2="807"/>
      <circle cx="400" cy="807" r="3" stroke="none"/>
      <line x1="170" y1="969" x2="630" y2="969"/>
      <circle cx="400" cy="969" r="3" stroke="none"/>
    </g>
  </svg>

  <div class="brand"><span class="brand-dot"></span><span class="brand-name">Tobin's Jewelry Studio</span></div>

  <div class="sale-disc"></div>
  <p class="center sale-kicker">MOVING</p>
  <p class="center sale-word">SALE</p>
  <p class="center sale-upto">UP TO</p>
  <div class="sale-amount">
    <span class="sale-number">80</span>
    <span class="sale-off"><span class="sale-percent">%</span><span class="sale-offword">OFF</span></span>
  </div>

  <div class="start-disc">
    <span class="start-label">START</span>
    <span class="start-date">Sept. 8th</span>
  </div>

  <h2 class="center heading move-heading">WE ARE MOVING</h2>
  <p class="center move-text">to our city's downtown which is only 1 mile<br>away from our current address.</p>

  <h2 class="center heading location-heading">CURRENT LOCATION</h2>
  <p class="center address">4785 Cresthaven Blvd. Dunmore, Ca 94318</p>
  <p class="center phone">(415)826-3319</p>
  <p class="center opening">New downtown location opening Nov. 1st</p>

  <p class="center tagline">WE CREATES, SELLS, &amp; REPAIRS FINE JEWELRY</p>
</main>
</body>
</html>
```